Corinne Bracket tutoring Advertising package - flyers, posters, business card and logo

I am looking for a flyer design for my tutoring business, it needs to explain what tutoring services I offer, how much I charge, why my services are worthwhile, it should include some photos of me and the tutoring centre,

It needs to include my phone number and my website. It should quote from some of the testimonials I have received from parents and children.

My website is www.corinnebracket-example.com My Facebook page can be found at https://www.facebook.com/corinnebrackettutoring These pages include a range of photos and quotes that you can use.

I am not sure about the colours and designs that I would like, that's why I'm using Sketchmarket!
I'm looking to appeal to parents inform them of my skills and experience.

I'm charging $45 for sessions of an hour and 15 minutes. 2 sessions per week will cost $80. I tutor Monday to Friday afternoons and evenings along with all day Saturdays. The assessment is free.

I tutor children from K-9 in English and Maths. I'm mainly aiming at parents whose children are struggling a little bit at school although I can help children who are doing well too.
I am highly skilled at helping children who can't read, I have a comprehensive program, the Pemberly program, that specifically teaches children the skills they need to read fluently and successfully.

Similarly I have had a lot of experience at helping children improve their Maths skills. I am well resourced with a wide range of hands on resources, paper resources and electronic resources.

Children will get better GRESTO results if I tutor them (GRESTO is the national series of tests in Australia).

I'm after a DL double sided flyer, and an A4 flyer. I'm also looking for two A2 posters and two A3 posters. Finally, I want a business card too. I don't have a logo for the business and I'd love to have one!

Target Market(s)

Parents of school aged children

Industry/Entity Type

Education

Colors

Designer to choose colors to be used in the design.

Requirements
Must have
• my name, my photo, length and cost of my sessions, email and phone contact details. Subjects and age ranges that I teach, times that I tutor. Website and/or Facebook page references. Quotes from Testimonials
Nice to have
• The A2 and A3 posters should complement each other.

```html
<!DOCTYPE html>
<html lang="en">
<head>
<meta charset="utf-8">
<title>Corinne Bracket Tutoring – Flyer</title>
<link href="https://fonts.googleapis.com/css2?family=Source+Sans+3:wght@300;400;600;700;800&family=Oswald:wght@500&display=swap" rel="stylesheet">
<style>
:root{
  --backdrop:#8a8a8a;
  --paper:#ffffff;
  --sky:#1f87c9;
  --navy:#1b5f95;
  --coral:#ee5a6f;
  --ink:#1b1b1b;
  --tick:#ffe52a;
  --photo-warm:#c98a5e;
  --photo-light:#e9e2d6;
}
*{box-sizing:border-box;margin:0;padding:0}
html,body{width:945px;height:1200px;overflow:hidden;background:var(--backdrop)}
body{position:relative;font-family:"Source Sans 3",Arial,sans-serif;color:var(--ink)}
.flyer{position:absolute;left:80px;top:92px;width:785px;height:1015px;background:var(--paper);overflow:hidden}
.abs{position:absolute}

/* service strip */
.services{left:0;top:18px;width:785px;height:42px}
.service{position:absolute;top:0;text-align:center;font-weight:700;font-size:16px;line-height:19px}
.divider{position:absolute;top:0;width:5px;height:40px;background:var(--coral)}

/* brand */
.brand{left:338px;top:72px;display:flex;align-items:center;gap:16px;z-index:2}
.brand-mark{width:60px;height:60px;background:var(--sky)}
.brand-name{color:var(--sky);font-weight:700;text-transform:uppercase;line-height:1}
.brand-name .line1{display:block;font-size:27px;letter-spacing:.5px}
.brand-name .line2{display:block;font-size:46px;margin-top:2px}

/* hero */
.hero{left:0;top:185px;width:785px;height:343px;background:var(--sky)}
.hero-photo{left:0;top:105px;width:295px;height:423px;border-radius:120px 120px 0 0;
  background:radial-gradient(ellipse at 55% 25%,#f6d9c4 0%,#e9b999 26%,#c9354a 58%,#b52a38 100%)}
.headline{left:313px;top:30px;color:#fff;font-weight:700;font-size:33px;line-height:36px}
.benefits{left:522px;top:18px;width:240px;list-style:none;color:#fff;font-weight:700;font-size:14.5px;line-height:17px}
.benefits li{position:relative;padding-left:22px;margin-bottom:8px}
.benefits svg{position:absolute;left:0;top:3px}
.promise{left:360px;top:222px;width:410px;text-align:center;color:#fff;text-transform:uppercase}
.promise .soft{display:block;font-weight:300;font-size:30px;line-height:33px}
.promise .strong{display:block;font-weight:800;font-size:48px;line-height:48px}

/* pricing */
.pricing{left:0;top:528px;width:785px;height:178px;background:var(--coral);color:#fff}
.price{left:40px;font-weight:800;font-size:22px;line-height:24px}
.price-note{left:40px;font-size:12px}
.hours{left:40px;top:124px;font-weight:700;font-size:13.5px;line-height:17px}
.room-photo{top:16px;height:147px;border:5px solid #fff;
  background:linear-gradient(160deg,var(--photo-light) 0%,var(--photo-warm) 55%,#8a5634 100%)}

/* testimonials */
.testimonials{left:0;top:706px;width:785px;height:224px;background:var(--navy);color:#fff}
.testimonials h2{position:absolute;left:0;top:16px;width:785px;text-align:center;font-weight:800;font-size:21px;text-transform:uppercase;letter-spacing:.2px}
.quote{top:55px;font-size:12.5px;line-height:14.2px;font-weight:400}
.quote cite{display:block;text-align:right;font-style:normal;font-weight:700;margin-top:2px}

/* contact */
.assessment{left:38px;top:923px;width:239px;height:36px;background:var(--coral);border:3px solid #fff;
  color:#fff;font-family:"Oswald","Arial Narrow",sans-serif;font-weight:500;font-size:22px;line-height:30px;text-align:center;text-transform:uppercase}
.cta{left:38px;top:964px;width:239px;text-align:center;color:var(--sky);font-weight:800;font-size:20px;text-transform:uppercase}
.phone{left:296px;top:940px;display:flex;align-items:center;gap:10px;color:var(--coral);font-weight:800;font-size:35px;line-height:1}
.website{left:296px;top:982px;width:300px;text-align:center;color:var(--navy);font-weight:700;font-size:15px}
.detail{left:597px;font-size:13px;line-height:16px;color:var(--ink)}
.detail svg{position:absolute;left:0;top:2px}
.detail span{display:block;padding-left:16px}
</style>
</head>
<body>
<main class="flyer">

  <div class="abs services">
    <div class="service" style="left:40px;width:100px">Grades<br>from K-9</div>
    <div class="divider" style="left:149px"></div>
    <div class="service" style="left:172px;width:175px">Maths English and<br>Maths Enrichments</div>
    <div class="divider" style="left:368px"></div>
    <div class="service" style="left:385px;width:150px">Homework Help<br>School Test Prep</div>
    <div class="divider" style="left:547px"></div>
    <div class="service" style="left:560px;width:200px">Algebra / Trig<br>Calculus / Geometry</div>
  </div>

  <div class="abs brand">
    <div class="brand-mark"></div>
    <div class="brand-name"><span class="line1">Corinne Bracket</span><span class="line2">Tutoring</span></div>
  </div>

  <section class="abs hero">
    <h1 class="abs headline">Tutoring<br>That works</h1>
    <ul class="abs benefits">
      <li><svg width="15" height="11" viewBox="0 0 15 11"><path d="M1 5.5l4.5 4L14 1" fill="none" stroke="var(--tick)" stroke-width="3"/></svg>Pemberly program to help your child read.</li>
      <li><svg width="15" height="11" viewBox="0 0 15 11"><path d="M1 5.5l4.5 4L14 1" fill="none" stroke="var(--tick)" stroke-width="3"/></svg>Focus on Specific learning areas</li>
      <li><svg width="15" height="11" viewBox="0 0 15 11"><path d="M1 5.5l4.5 4L14 1" fill="none" stroke="var(--tick)" stroke-width="3"/></svg>Individual Program design</li>
      <li><svg width="15" height="11" viewBox="0 0 15 11"><path d="M1 5.5l4.5 4L14 1" fill="none" stroke="var(--tick)" stroke-width="3"/></svg>Reading, writing, spelling, grammer and maths</li>
      <li><svg width="15" height="11" viewBox="0 0 15 11"><path d="M1 5.5l4.5 4L14 1" fill="none" stroke="var(--tick)" stroke-width="3"/></svg>Positive and supportive learning environment designed to promote confidence</li>
    </ul>
    <p class="abs promise">
      <span class="soft">Make this school year</span>
      <span class="strong">Greater than</span>
      <span class="soft">Last year....</span>
    </p>
  </section>

  <div class="abs hero-photo" role="img" aria-label="Smiling schoolgirl in a red tartan uniform with a backpack, giving a thumbs up"></div>

  <section class="abs pricing">
    <p class="abs price" style="top:16px">$45 PER SESSION</p>
    <p class="abs price-note" style="top:40px">(one hour and 15 minutes)</p>
    <p class="abs price" style="top:68px">$80 TWO SESSIONS</p>
    <p class="abs price-note" style="top:92px">per week</p>
    <p class="abs hours">Monday to Friday afternoons and<br>evenings along with all day Saturdays.</p>
    <div class="abs room-photo" style="left:304px;width:208px" role="img" aria-label="Tutoring room with bookshelves and a round wooden table"></div>
    <div class="abs room-photo" style="left:531px;width:211px" role="img" aria-label="Tutoring centre study area with shelves and desks"></div>
  </section>

  <section class="abs testimonials">
    <h2>What parents are saying about Corinne Tutouring</h2>
    <blockquote class="abs quote" style="left:43px;width:190px">Our son has been tutored by Corinne now for the past 2 years - we have noticed a big improvement with his spelling and mathematics. This has also helped our son's confidence in his daily schooling and he now has started to enjoy school again . Thanks Corinne<cite>Mark and Helen Dorsey</cite></blockquote>
    <blockquote class="abs quote" style="left:263px;width:208px">Our children love going to Corinne's!! Yes you read that right - they LOVE going to learn! Corinne has the ability to tap into each child's strengths and weaknesses and he makes learning fun! Our children's grades have improved more so, our son just got awarded a distinction in a science competition! Thanks so much Corinne<cite>Paula Kemp</cite></blockquote>
    <blockquote class="abs quote" style="left:505px;width:240px">My daughter has been seeing Corinne for about a year now. The improvement in her reading and writing is amazing. She has gone from getting 2s on her report cards to getting 4s. I'm always telling people Corinne is one of those people who you just have a conversation with and you learn something. I plan to start tutoring for my 2 boys with Corinne asap. He is always friendly and understanding of life's circumstances.<cite>Nadia Forster</cite></blockquote>
  </section>

  <p class="abs assessment">Assessment is free</p>
  <p class="abs cta">Contact me today!</p>

  <p class="abs phone">
    <svg width="28" height="20" viewBox="0 0 28 20" aria-hidden="true"><path d="M2 7c0-4 6-5 12-5s12 1 12 5v2h-6V6H8v3H2z M7 10h14l3 8H4z" fill="var(--navy)"/></svg>
    0400 555 218
  </p>
  <p class="abs website">www.corinnebracket-example.com</p>

  <p class="abs detail" style="top:945px">
    <svg width="10" height="13" viewBox="0 0 10 13" aria-hidden="true"><path d="M5 0a5 5 0 0 1 5 5c0 3-5 8-5 8S0 8 0 5a5 5 0 0 1 5-5z" fill="var(--sky)"/><circle cx="5" cy="5" r="2" fill="#fff"/></svg>
    <span>14 Harbour Lane Lakeside<br>NSW 2000.</span>
  </p>
  <p class="abs detail" style="top:982px">
    <svg width="11" height="9" viewBox="0 0 11 9" aria-hidden="true"><rect width="11" height="9" rx="1" fill="var(--sky)"/><path d="M0.5 1l5 4 5-4" fill="none" stroke="#fff" stroke-width="1"/></svg>
    <span>corinnebracket@example.com</span>
  </p>

</main>
</body>
</html>
```